Counseling business card, clean but alluring

I need it to appeal to all ages and men. I’m planning to use my current logo. I like crisp and clean. Possibly some shimmer. My website is harborleafwellness.net

Contact Information for Business Card

Marissa "Missy" Dolan Pryce, LPC, RPT

harborleafwellness.net

28159 Larkspur Avenue, Suite 407
Cedar Hollow TX 75094

469-315-2984 | missy@harborleafwellness.net

Colors
0355a3
85cae6
fbee3e
ffffff
33b8a4
0692cd

Requirements
Must have
• My logo

```html
<!DOCTYPE html>
<html lang="en">
<head>
<meta charset="utf-8">
<title>Harborleaf Wellness – Business Card</title>
<link href="https://fonts.googleapis.com/css2?family=Lato:ital,wght@0,400;1,700&family=Marcellus&display=swap" rel="stylesheet">
<style>
  :root {
    --brand-blue: #0355a3;
    --ink-blue: #1a4fa0;
    --rule-blue: #2b5aa8;
    --ink-dark: #1e1e1e;
    --paper: #ffffff;
    --stage: #e9ecef;
  }
  * { box-sizing: border-box; margin: 0; padding: 0; }
  html, body {
    width: 1200px; height: 900px; overflow: hidden;
    background: var(--stage);
  }
  .canvas { position: relative; width: 1200px; height: 900px; }
  .card {
    position: absolute; left: 250px; width: 700px; height: 400px;
    border-radius: 22px; overflow: hidden;
    box-shadow: 0 6px 18px rgba(0,0,0,.18);
  }
  /* front */
  .card-front { top: 35px; background: var(--brand-blue); }
  .front-brand {
    position: absolute; right: 56px; top: 170px;
    display: flex; align-items: center; gap: 22px;
  }
  .front-brand .mark-dot {
    width: 26px; height: 26px; border-radius: 50%; background: var(--paper);
  }
  .front-brand .brand-name {
    font-family: "Marcellus", serif; font-size: 56px; color: var(--paper);
    letter-spacing: 1px; white-space: nowrap;
  }
  /* back */
  .card-back { top: 465px; background: var(--paper); }
  .back-brand {
    position: absolute; left: 44px; top: 64px;
    display: flex; align-items: center; gap: 16px;
  }
  .back-brand .mark-dot {
    width: 22px; height: 22px; border-radius: 50%; background: var(--ink-blue);
  }
  .back-brand .brand-name {
    font-family: "Marcellus", serif; font-size: 50px; color: var(--ink-blue);
    white-space: nowrap;
  }
  .brand-rule {
    position: absolute; left: 44px; right: 40px; top: 138px;
    border-top: 1.5px solid var(--rule-blue);
  }
  .holder-name {
    position: absolute; left: 44px; top: 200px;
    font-family: "Lato", sans-serif; font-weight: 700; font-style: italic;
    font-size: 26px; color: var(--ink-blue); white-space: nowrap;
  }
  .name-rule {
    position: absolute; left: 44px; width: 470px; top: 240px;
    border-top: 1.5px solid var(--rule-blue);
  }
  .contact-list {
    position: absolute; left: 44px; top: 254px; list-style: none;
    font-family: "Lato", sans-serif; font-size: 19px; color: var(--ink-dark);
  }
  .contact-list li {
    display: flex; align-items: center; gap: 16px; height: 34px; white-space: nowrap;
  }
  .contact-list svg { width: 20px; height: 20px; fill: var(--ink-blue); flex: none; }
  .address {
    position: absolute; right: 44px; top: 262px; text-align: left;
    font-family: "Lato", sans-serif; font-style: normal; font-weight: 400;
    font-size: 19px; line-height: 1.35; color: var(--ink-dark); white-space: nowrap;
  }
</style>
</head>
<body>
<main class="canvas">
  <section class="card card-front" aria-label="Card front">
    <div class="front-brand">
      <span class="mark-dot"></span>
      <span class="brand-name">Harborleaf Wellness</span>
    </div>
  </section>

  <section class="card card-back" aria-label="Card back">
    <div class="back-brand">
      <span class="mark-dot"></span>
      <span class="brand-name">Harborleaf Wellness</span>
    </div>
    <div class="brand-rule"></div>

    <h1 class="holder-name">Marissa “Missy” Dolan Pryce, LPC, RPT</h1>
    <div class="name-rule"></div>

    <ul class="contact-list">
      <li>
        <svg viewBox="0 0 24 24" aria-hidden="true"><path d="M6.6 10.8a15.1 15.1 0 0 0 6.6 6.6l2.2-2.2a1 1 0 0 1 1-.25 11.4 11.4 0 0 0 3.6.57 1 1 0 0 1 1 1V20a1 1 0 0 1-1 1A17 17 0 0 1 3 4a1 1 0 0 1 1-1h3.5a1 1 0 0 1 1 1c0 1.25.2 2.45.57 3.570a1 1 0 0 1-.25 1z"/></svg>
        <span>469-315-2984</span>
      </li>
      <li>
        <svg viewBox="0 0 24 24" aria-hidden="true"><path d="M2 5h20v14H2z M3.5 6.5 12 12.5l8.5-6" fill="none" stroke="#1a4fa0" stroke-width="2"/></svg>
        <span>missy@harborleafwellness.net</span>
      </li>
      <li>
        <svg viewBox="0 0 24 24" aria-hidden="true"><circle cx="12" cy="12" r="9" fill="none" stroke="#1a4fa0" stroke-width="2"/><path d="M3 12h18M12 3c3 3 3 15 0 18M12 3c-3 3-3 15 0 18" fill="none" stroke="#1a4fa0" stroke-width="1.6"/></svg>
        <span>harborleafwellness.net</span>
      </li>
    </ul>

    <address class="address">
      28159 Larkspur Avenue, Suite 407<br>
      Cedar Hollow TX 75094
    </address>
  </section>
</main>
</body>
</html>
```